Customizable Gift Note Card Design

I need a gift note card designed for my Healthy Snacks Care Package company. I need to be able to customize each card with the customer's gift message to the recipient and print to a standard printer.

The card should be single-sided 5 x 7, include our logo, keep colors and graphics simple since they will be printed for each individual order on a standard printer. I would like the following quote to be included in a small and subtle way: "Food is symbolic of love when words are inadequate." —Bertram K. Osslund. Our website thebrightpantrybites.example should also be included.

I have included pictures of our product packaging for reference.

Target Market(s)

Gift recipients: Students, people recovering from illness, housewarming, thank you gifts...etc.

Industry/Entity Type

It Company

Colors

Designer to choose colors to be used in the design.

Requirements
Must have
• We are looking for a simple, cute and elegant gift card that reflects our branding. Must be customizable and printable on a standard printer.
• Must be single-sided 5x7.

```html
<!DOCTYPE html>
<html lang="en">
<head>
<meta charset="utf-8">
<title>The Bright Pantry – Gift Note Card</title>
<link rel="stylesheet" href="https://fonts.googleapis.com/css2?family=Lato:wght@400;700&display=swap">
<style>
  :root {
    --paper: #eef0ef;
    --paper-shade: #e2e5e4;
    --ink: #0b0d0e;
    --accent-red: #8e0702;
    --white: #ffffff;
  }
  * { margin: 0; padding: 0; box-sizing: border-box; }
  html, body {
    width: 857px;
    height: 1200px;
    overflow: hidden;
    background: var(--paper);
  }
  .gift-card {
    position: relative;
    width: 857px;
    height: 1200px;
    background: var(--paper);
    font-family: "Lato", sans-serif;
  }
  .backdrop-motif {
    position: absolute;
    inset: 0;
    background:
      repeating-linear-gradient(90deg, var(--paper-shade) 0 62px, var(--paper) 62px 91px);
    opacity: 0.9;
  }
  .brand-lockup {
    position: absolute;
    left: 150px;
    top: 712px;
    display: flex;
    align-items: center;
    gap: 26px;
  }
  .brand-dot {
    width: 92px;
    height: 92px;
    border-radius: 50%;
    background: var(--ink);
    flex: none;
  }
  .brand-name {
    font-size: 62px;
    font-weight: 700;
    color: var(--ink);
    letter-spacing: 0.3px;
    line-height: 1;
    white-space: nowrap;
  }
  .footer-bands {
    position: absolute;
    left: 0;
    top: 0;
    width: 857px;
    height: 1200px;
  }
  .quote-block {
    position: absolute;
    left: 0;
    right: 0;
    top: 1013px;
    text-align: center;
    color: var(--white);
    font-size: 32px;
    font-weight: 400;
    line-height: 40px;
    white-space: nowrap;
  }
</style>
</head>
<body>
  <main class="gift-card">
    <div class="backdrop-motif" role="img" aria-label="Faint light-grey repeating brand motif pattern covering the card background"></div>

    <div class="brand-lockup">
      <span class="brand-dot"></span>
      <span class="brand-name">The Bright Pantry</span>
    </div>

    <svg class="footer-bands" viewBox="0 0 857 1200" aria-hidden="true">
      <polygon points="0,880 479,921 0,962" fill="var(--accent-red)"/>
      <polygon points="0,962 857,889 857,1146 0,1146" fill="var(--ink)"/>
    </svg>

    <p class="quote-block">
      Food is symbolic of love when words are inadequate.<br>
      —Bertram K. Osslund
    </p>
  </main>
</body>
</html>
```